Buch-/E-Book-Cover für Reise- und Liebesroman
Zielgruppe
Das eBook 'Der stille Hafen' ist ein Reise- und Liebesroman, ein Ausbruch aus dem Lebensalltag und einer belastenden Situation, das Eintauchen in ein fernes Land; Mystik, zu sich zurückfinden, eine traumatische Erfahrung überwinden.
Inhalt: Die Berlinerin Ilse Brandauer überwindet durch eine mystische Thailandreise eine belastende Situation.
Ilse: 49 Jahre alt, lockiges, von silbrigen Fäden durchzogenes helles Haar. Eher zeitlos wirkend. Groß und schlank.
Zielgruppe: Frauen (und auch Männer) zwischen 28 und 65
Aufgabenstellung
Die Leser dieser Titel sollen das 'Der stille Hafen' als Reise- und Liebesroman erkennen. Deshalb sollte Anmutung und Aufbau wiedererkennbar sein (aber nicht kopiert!):
'Die Nebeltochter', https://www.buchkiosk-beispiel.example/dp/X481QWZKPM/

```html
<!DOCTYPE html>
<html lang="de">
<head>
<meta charset="utf-8">
<title>Der stille Hafen – Henrike Solberg</title>
<link rel="stylesheet" href="https://fonts.googleapis.com/css2?family=Cinzel+Decorative:wght@700&family=Oswald:wght@400;500&display=swap">
<style>
  :root {
    --sky-top: #54588c;
    --sky-violet: #8a6c9c;
    --sky-red: #e8503c;
    --sky-orange: #f27a4e;
    --sky-glow: #f8a676;
    --horizon-haze: #f4b0a0;
    --horizon-line: #c98a9a;
    --water-bright: #f6d2d6;
    --water-pink: #eaa8c0;
    --water-lilac: #c08ad2;
    --water-blue: #5a70e0;
    --water-cyan: #8ec8d8;
    --shore-dark: #2a2f5c;
    --text-light: #ffffff;
    --title-edge: #1d3a7a;
  }
  * { margin: 0; padding: 0; box-sizing: border-box; }
  html, body {
    width: 818px;
    height: 1200px;
    overflow: hidden;
    background: var(--shore-dark);
  }
  .cover {
    position: relative;
    width: 818px;
    height: 1200px;
    overflow: hidden;
  }
  .cover-scene {
    position: absolute;
    inset: 0;
    background:
      /* dark rocks on the shore */
      radial-gradient(ellipse 360px 70px at 330px 1110px, rgba(42,47,92,0.85), rgba(42,47,92,0) 70%),
      radial-gradient(ellipse 260px 90px at 40px 1190px, rgba(30,32,70,0.9), rgba(30,32,70,0) 70%),
      /* sun reflection on the water */
      radial-gradient(ellipse 380px 110px at 220px 880px, rgba(255,236,232,0.75), rgba(255,236,232,0) 70%),
      radial-gradient(ellipse 300px 60px at 200px 1030px, rgba(246,140,170,0.55), rgba(246,140,170,0) 70%),
      /* clear water on the right */
      radial-gradient(ellipse 360px 260px at 760px 1000px, rgba(142,200,216,0.6), rgba(142,200,216,0) 70%),
      /* cloud glow in the sky */
      radial-gradient(ellipse 460px 130px at 260px 170px, rgba(232,80,60,0.85), rgba(232,80,60,0) 70%),
      radial-gradient(ellipse 520px 120px at 620px 330px, rgba(240,110,70,0.7), rgba(240,110,70,0) 70%),
      radial-gradient(ellipse 420px 110px at 120px 470px, rgba(248,166,118,0.8), rgba(248,166,118,0) 70%),
      radial-gradient(ellipse 500px 140px at 560px 600px, rgba(236,90,70,0.7), rgba(236,90,70,0) 70%),
      radial-gradient(ellipse 380px 90px at 700px 60px, rgba(120,110,170,0.7), rgba(120,110,170,0) 70%),
      /* sky, horizon and sea */
      linear-gradient(180deg,
        var(--sky-top) 0%,
        var(--sky-violet) 7%,
        var(--sky-red) 17%,
        var(--sky-orange) 30%,
        var(--sky-glow) 42%,
        var(--sky-orange) 52%,
        var(--sky-red) 58%,
        var(--horizon-haze) 63%,
        var(--horizon-line) 65.3%,
        var(--water-bright) 65.6%,
        var(--water-bright) 72%,
        var(--water-pink) 80%,
        var(--water-lilac) 86%,
        var(--water-blue) 92%,
        var(--shore-dark) 100%);
  }
  .author {
    position: absolute;
    top: 38px;
    left: 0;
    width: 100%;
    text-align: center;
    font-family: "Oswald", sans-serif;
    font-weight: 500;
    font-size: 66px;
    line-height: 1;
    letter-spacing: 0.15em;
    color: var(--text-light);
    text-transform: uppercase;
  }
  .title {
    position: absolute;
    top: 262px;
    left: 0;
    width: 100%;
    text-align: center;
    font-family: "Cinzel Decorative", serif;
    font-weight: 700;
    color: var(--text-light);
    text-shadow: 2px 2px 0 var(--title-edge);
    line-height: 0.95;
  }
  .title-line { display: block; }
  .title-line--short { font-size: 152px; }
  .title-line--mid { font-size: 142px; }
  .title-line--long { font-size: 160px; margin-top: 14px; }
  .genre {
    position: absolute;
    left: 62px;
    bottom: 22px;
    font-family: "Oswald", sans-serif;
    font-weight: 500;
    font-size: 60px;
    line-height: 1;
    letter-spacing: 0.08em;
    color: var(--text-light);
    text-transform: uppercase;
  }
</style>
</head>
<body>
  <main class="cover">
    <div class="cover-scene" role="img" aria-label="Foto: tropischer Sonnenuntergang über stillem Meer mit Holzsteg und überdachten Pavillons"></div>
    <p class="author">Henrike Solberg</p>
    <h1 class="title">
      <span class="title-line title-line--short">Der</span>
      <span class="title-line title-line--mid">stille</span>
      <span class="title-line title-line--long">Hafen</span>
    </h1>
    <p class="genre">Roman</p>
  </main>
</body>
</html>
```